Business Card Design Project

We need a business card design for our company kB7 s.r.o. The company is based in Slovakia and selling massage, yoga and meditation accessories online and offline. At the place where the offices are, we have a yoga studio, massage room, show room and shop as well. We will give the business card for customers who visit our shop or show room personally and for the new suppliers of demanded products we are visiting in the future.
I would like to have:
- small logo and datas on one side
- big logo and our main e-shops on the other side:
- www.pohodlnelavice.sk
- www.relaxnipultiky.cz
Datas:
Peter Kolar, MSc. / CEO
kB7 s.r.o.
Borovicová 742/3
938 05 Lipovská Nivka
Slovak republic (Slovakia)
Office tel.: +421 (0) 917 604 382
Private tel.: +421 (0) 911 758 026
E-mail: info@kb7.sk
Web: www.kb7.sk
It is up to you if you use graphics emphasizing our profile or leave it simple and modern without pics. Looking forward to receiving your designs! Thank You!

```html
<!DOCTYPE html>
<html lang="sk">
<head>
<meta charset="utf-8">
<title>kB7 s.r.o. – business card</title>
<link rel="stylesheet" href="https://fonts.googleapis.com/css2?family=Lato:wght@400;700&display=swap">
<style>
  :root {
    --stage: #2e2f31;
    --card: #ffffff;
    --ink: #1e1f22;
    --slate: #4c5562;
    --muted: #5f6872;
    --orange: #f08122;
    --rule: #c9ccd0;
  }
  * { box-sizing: border-box; margin: 0; padding: 0; }
  html, body { width: 1200px; height: 926px; overflow: hidden; }
  body {
    background: var(--stage);
    font-family: "Lato", sans-serif;
    color: var(--ink);
    position: relative;
  }
  .card {
    position: absolute;
    left: 274px;
    width: 652px;
    height: 313px;
    background: var(--card);
    border-radius: 14px;
  }
  .card--front { top: 118px; }
  .card--back  { top: 456px; }

  .brand {
    position: absolute;
    display: flex;
    align-items: center;
    gap: 10px;
    color: var(--slate);
    font-weight: 700;
    letter-spacing: 1px;
    line-height: 1;
  }
  .brand__dot {
    border-radius: 50%;
    background: var(--orange);
    flex: none;
  }
  .card--front .brand {
    left: 50%;
    top: 44%;
    transform: translate(-50%, -50%);
    font-size: 84px;
  }
  .card--front .brand__dot { width: 22px; height: 22px; }

  .eshops {
    position: absolute;
    left: 0; right: 0;
    top: 80%;
    text-align: center;
    font-size: 16px;
    font-weight: 700;
    letter-spacing: 1.2px;
    color: var(--muted);
  }

  .card--back .brand {
    left: 9%;
    top: 66%;
    font-size: 58px;
  }
  .card--back .brand__dot { width: 15px; height: 15px; }

  .divider {
    position: absolute;
    left: 42.5%;
    top: 47%;
    height: 48%;
    width: 1px;
    background: var(--rule);
  }

  .name-band {
    position: absolute;
    left: 50.5%;
    top: 14%;
    width: 47%;
    height: 54px;
    background: var(--orange);
    color: #fff;
    padding: 6px 40px 0 16px;
    text-align: right;
    box-shadow: 0 12px 14px -8px rgba(0,0,0,0.35);
  }
  .name-band__name { font-size: 21px; line-height: 26px; white-space: nowrap; }
  .name-band__name strong { font-weight: 700; }
  .name-band__title { font-size: 14px; font-weight: 700; }
  .name-band__company { font-size: 13px; font-weight: 700; line-height: 16px; }
  .name-band__icon { position: absolute; right: 18px; top: 10px; width: 14px; height: 14px; }

  .contacts {
    position: absolute;
    right: 4%;
    list-style: none;
    font-size: 16px;
    line-height: 20px;
    text-align: right;
    white-space: nowrap;
  }
  .contacts--lines { top: 46%; }
  .contacts--address { top: 76%; }
  .contacts li {
    display: flex;
    justify-content: flex-end;
    align-items: center;
    gap: 10px;
  }
  .contacts .icon { width: 15px; height: 15px; flex: none; }
  .contacts .icon--blank { visibility: hidden; }
  .icon { fill: var(--orange); }
</style>
</head>
<body>

<section class="card card--front" aria-label="Front side">
  <div class="brand"><span class="brand__dot"></span>kB7</div>
  <p class="eshops">www.pohodlnelavice.sk / www.relaxnipultiky.cz</p>
</section>

<section class="card card--back" aria-label="Back side">
  <div class="name-band">
    <div class="name-band__name">Peter <strong>Kolar</strong>, <span class="name-band__title">MSc. / CEO</span></div>
    <div class="name-band__company">kB7 s.r.o.</div>
    <svg class="name-band__icon" viewBox="0 0 16 16" fill="#fff" aria-hidden="true">
      <circle cx="8" cy="5" r="3.6"/><path d="M1 16c0-4 3-6.5 7-6.5s7 2.5 7 6.5z"/>
    </svg>
  </div>

  <div class="brand"><span class="brand__dot"></span>kB7</div>
  <div class="divider"></div>

  <ul class="contacts contacts--lines">
    <li>+421 (0) 917 604 382 (Office)
      <svg class="icon" viewBox="0 0 16 16" aria-hidden="true"><path d="M1 6c0-2 3-3.5 7-3.5s7 1.5 7 3.5v1.2h-3.5V5.6H4.5v1.6H1z"/><path d="M3 14l1.5-6h7L13 14z"/></svg></li>
    <li>+421 (0) 911 758 026 (Private)
      <svg class="icon" viewBox="0 0 16 16" aria-hidden="true"><path d="M1 6c0-2 3-3.5 7-3.5s7 1.5 7 3.5v1.2h-3.5V5.6H4.5v1.6H1z"/><path d="M3 14l1.5-6h7L13 14z"/></svg></li>
    <li>info@kb7.sk
      <svg class="icon" viewBox="0 0 16 16" aria-hidden="true"><path d="M1 3h14v10H1z"/><path d="M1.5 3.5L8 9l6.5-5.5" fill="none" stroke="#fff" stroke-width="1.3"/></svg></li>
    <li>www.kb7.sk
      <svg class="icon" viewBox="0 0 16 16" aria-hidden="true"><path d="M1 2h14v10H1zM2.5 3.5v7h11v-7z" fill-rule="evenodd"/><path d="M5 14h6v1.2H5z"/></svg></li>
  </ul>

  <ul class="contacts contacts--address">
    <li>Borovicová 742/3,
      <svg class="icon" viewBox="0 0 16 16" aria-hidden="true"><path d="M8 0.5a5.5 5.5 0 0 1 5.5 5.5C13.5 10 8 15.5 8 15.5S2.5 10 2.5 6A5.5 5.5 0 0 1 8 0.5zM8 3.8a2.2 2.2 0 1 0 0 4.4a2.2 2.2 0 0 0 0-4.4z" fill-rule="evenodd"/></svg></li>
    <li>938 05 Lipovská Nivka,<span class="icon icon--blank"></span></li>
    <li>Slovak republic (Slovakia)<span class="icon icon--blank"></span></li>
  </ul>
</section>

</body>
</html>
```